Webdesign für ein Dachdeckerbetrieb
Zielgruppe
Wir sind ein Dachdeckerbetrieb.
Zielgruppe sind öffentliche Auftrageber , Hausverwaltungen und private Hausbesitzer.
Aufgabenstellung
Die Seite sollte übersichtlich sein. Nicht zuviele Menüs durch die man klicken muss.
Bilder können wir liefern .
Nach Vorgabe des Designers beschaffen wir die Bilder .
Logo ist vorhanden.

```html
<!DOCTYPE html>
<html lang="de">
<head>
<meta charset="utf-8">
<title>Kestner Dachbau – Über uns</title>
<link href="https://fonts.googleapis.com/css2?family=Roboto:wght@300;400;500;700&display=swap" rel="stylesheet">
<style>
:root{
  --green:#92ae24;
  --dark:#333538;
  --hero:#4a4b4d;
  --text:#333333;
  --muted:#6d6d6d;
  --light:#f0f0f0;
  --white:#ffffff;
}
*{margin:0;padding:0;box-sizing:border-box}
html,body{width:736px;height:1200px;overflow:hidden}
body{font-family:'Roboto',sans-serif;color:var(--text);background:var(--white);position:relative}
.abs{position:absolute}
/* header */
.header{left:0;top:0;width:736px;height:44px;background:var(--white)}
.brand{left:144px;top:12px;display:flex;align-items:center;gap:4px;font-weight:700;font-size:13px;color:var(--green);letter-spacing:-.2px}
.brand .sq{width:9px;height:9px;background:var(--green)}
.nav{top:17px;font-size:6.6px;color:var(--text)}
.nav.active{color:var(--green);font-weight:500}
.wa-box{left:520px;top:13px;width:72px;height:17px;background:var(--dark);color:var(--white)}
.wa-box .dot{position:absolute;left:4px;top:3px;width:11px;height:11px;border:1.2px solid var(--white);border-radius:50%}
.wa-box .lbl{position:absolute;left:20px;top:2px;font-size:5px;color:var(--green);font-weight:500}
.wa-box .num{position:absolute;left:20px;top:8px;font-size:6.6px}
/* hero */
.hero{left:0;top:44px;width:736px;height:128px;background:linear-gradient(160deg,#55565a,#3f4042 60%,#4a4b4d)}
.hero-title{left:0;width:736px;top:90px;text-align:center;font-size:19px;font-weight:700;color:var(--white);letter-spacing:-.6px}
.hero-sub{left:305px;top:114px;width:124px;height:13px;background:rgba(40,40,42,.6);text-align:center;font-size:7.5px;line-height:13px;color:var(--white)}
.hero-sub b{color:var(--green);font-weight:400}
/* intro */
.photo{background:linear-gradient(135deg,#b9c2cc 0%,#c96a45 45%,#6d6f72 100%);border-radius:4px}
.tag{background:var(--dark);color:var(--white);font-size:7.5px;padding:0 7px;height:14px;line-height:14px}
.h2{font-weight:700;letter-spacing:-.5px;color:var(--text)}
.h2 em{font-style:normal;color:var(--green)}
.copy{font-size:6.5px;line-height:12.3px;color:var(--muted);font-weight:300}
.copy strong{font-weight:500;color:#555}
/* band */
.band{left:0;top:436px;width:736px;height:48px;background:var(--green);color:var(--white)}
.band-q{left:143px;top:18px;font-size:11.5px;font-weight:500}
.band-q span{font-weight:300;font-size:9.5px}
.band-tel{left:432px;top:19px;font-size:9px;font-weight:700}
/* team */
.team-bg{left:0;top:484px;width:736px;height:548px;background:var(--light)}
.member .pic{width:103px;height:107px;border-radius:3px}
.member .name{margin-top:12px;font-size:8.7px;font-weight:500;letter-spacing:-.3px;color:var(--text)}
.member .role{margin-top:2px;font-size:6.3px;color:var(--muted)}
.btn{left:329px;top:964px;width:77px;height:23px;background:var(--green);color:var(--white);font-size:6.3px;font-weight:500;text-align:center;line-height:23px;border-radius:2px}
/* footer */
.footer-line{left:0;top:1032px;width:736px;height:2px;background:#b9b9b9}
.footer{left:0;top:1034px;width:736px;height:166px;background:var(--dark);color:var(--white)}
.f-h{font-size:7.5px;font-weight:500}
.f-link{font-size:6.5px}
.f-link::before{content:"»";margin-right:4px}
.f-text{font-size:6px;line-height:12px}
.f-input{width:94px;height:15px;background:var(--white);font-size:5px;color:#999;padding-left:6px;line-height:15px}
.f-btn{width:49px;height:17px;border:1px solid var(--white);border-radius:2px;font-size:6px;font-weight:700;text-align:center;line-height:15px}
.social{width:12px;height:12px;border-radius:50%;background:var(--green)}
</style>
</head>
<body>

<header class="abs header">
  <div class="abs brand"><span class="sq"></span>KESTNER DACHBAU</div>
  <div class="abs nav" style="left:280px">Startseite</div>
  <div class="abs nav active" style="left:323px">Über uns</div>
  <div class="abs nav" style="left:366px">Referenzen</div>
  <div class="abs nav" style="left:414px">Leistungen</div>
  <div class="abs nav" style="left:463px">Kontakt</div>
  <div class="abs wa-box"><span class="dot"></span><span class="lbl">Kontakt Whatsapp</span><span class="num">0151-4470921</span></div>
</header>

<section class="abs hero" role="img" aria-label="Dunkle Dachschindeln als Hintergrund"></section>
<h1 class="abs hero-title">ÜBER UNS</h1>
<div class="abs hero-sub"><b>SIE</b> stehen bei uns <b>im Mittelpunkt</b></div>

<div class="abs photo" style="left:144px;top:213px;width:218px;height:175px" role="img" aria-label="Dachdecker verlegt rote Dachziegel auf Lattung"></div>
<div class="abs tag" style="left:407px;top:213px">Wir sind ihr Partner</div>
<h2 class="abs h2" style="left:406px;top:234px;font-size:18.5px;line-height:23px">Für <em>langlebige</em> und<br>moderne <em>Dächer</em></h2>
<p class="abs copy" style="left:407px;top:289px;width:180px">Unser Fachbetrieb ist Ihr zuverlässiger und fachkundiger Partner in allen Fragen rund um das Thema Bedachungen. Wir unterstützen Sie bei der Planung und Durchführung von sämtlichen Dachdeckerarbeiten.</p>
<p class="abs copy" style="left:407px;top:351px;width:172px">Bei unserer Arbeit überzeugen vor allem durch fachliche Kompetenz und viel Erfahrung. Wir arbeiten mit Ihnen zusammen – <strong>auch in schwindelerregender Höhe</strong>.</p>

<section class="abs band">
  <div class="abs band-q">Haben Sie weitere Fragen? <span>Wir haben die Antworten!</span></div>
  <svg class="abs" style="left:407px;top:16px" width="18" height="17" viewBox="0 0 18 17" fill="none" stroke="#fff" stroke-width="1.2"><path d="M4 1.5l3 3-2 2c1 2.5 3 4.5 5.5 5.5l2-2 3 3-2 2.5C7 15 2 10 1.5 3.5z"/><path d="M10 3a5 5 0 0 1 4 4M10 .5a7.5 7.5 0 0 1 6.5 6.5"/></svg>
  <div class="abs band-tel">von 8-17 Uhr: 0 62 14 - 57 20 48</div>
</section>

<section class="abs team-bg"></section>
<div class="abs tag" style="left:145px;top:522px">Ihre Aufgaben</div>
<h2 class="abs h2" style="left:144px;top:543px;font-size:19.5px">Lösen wir <em>individuell</em></h2>
<p class="abs copy" style="left:145px;top:574px;width:440px">Sie suchen starke und zuverlässige Dachdecker oder Zimmerer für Ihre Dachsanierung?<br>Unsere Dachdecker und Zimmerer bauen Ihnen ein qualitativ hochwertiges Dach, das Sie bei <strong>„Wind und Wetter“</strong> schützt und Ihnen ein sicheres und langlebiges Zuhause bietet.</p>

<div class="abs member" style="left:144px;top:634px"><div class="pic" style="background:linear-gradient(#3f6b3a,#a9b6c8)" role="img" aria-label="Porträt Geschäftsführer"></div><div class="name">Jonas Brenner</div><div class="role">Geschäftsführer</div></div>
<div class="abs member" style="left:259px;top:634px"><div class="pic" style="background:linear-gradient(#c9a67c,#3a3633)" role="img" aria-label="Porträt Buchhaltung"></div><div class="name">Ute Brenner</div><div class="role">Buchhaltung</div></div>
<div class="abs member" style="left:374px;top:634px"><div class="pic" style="background:linear-gradient(#2b3032,#1f2224)" role="img" aria-label="Porträt Schreinermeister"></div><div class="name">Lukas Brenner</div><div class="role">Schreinermeister</div></div>
<div class="abs member" style="left:489px;top:634px"><div class="pic" style="background:linear-gradient(#9c9e9f,#2a2a2c)" role="img" aria-label="Porträt Dachdecker"></div><div class="name">Felix Brenner</div><div class="role">Dachdecker</div></div>

<div class="abs member" style="left:144px;top:792px"><div class="pic" style="background:linear-gradient(#e4e4e4,#d9d4d0)" role="img" aria-label="Porträt Sachbearbeiterin"></div><div class="name">Karin Vogt</div><div class="role">Sachbearbeiterin</div></div>
<div class="abs member" style="left:258px;top:792px"><div class="pic" style="background:linear-gradient(#b8a898,#3b3d42)" role="img" aria-label="Porträt Schreinermeister"></div><div class="name">Dieter Haas</div><div class="role">Schreinermeister</div></div>
<div class="abs member" style="left:373px;top:792px"><div class="pic" style="background:linear-gradient(#ebebeb,#cfd2cf)" role="img" aria-label="Porträt Auszubildender"></div><div class="name">Nico Albers</div><div class="role">Azubi zum Dachdecker</div></div>
<div class="abs member" style="left:488px;top:792px"><div class="pic" style="background:linear-gradient(#c4a43a,#5b6f8c)" role="img" aria-label="Porträt Dachdecker"></div><div class="name">Sven Roder</div><div class="role">Dachdecker</div></div>

<div class="abs btn">Kontakt aufnehmen</div>

<div class="abs footer-line"></div>
<footer class="abs footer">
  <div class="abs f-h" style="left:155px;top:37px">Navigation</div>
  <div class="abs f-link" style="left:155px;top:54px">Startseite</div>
  <div class="abs f-link" style="left:155px;top:71px">Über uns</div>
  <div class="abs f-link" style="left:155px;top:89px">Referenzen</div>
  <div class="abs f-link" style="left:155px;top:106px">Leistungen</div>
  <div class="abs f-link" style="left:155px;top:123px">Kontakt</div>

  <div class="abs f-h" style="left:247px;top:37px">Rechtliches</div>
  <div class="abs f-link" style="left:247px;top:54px">Datenschutz</div>
  <div class="abs f-link" style="left:247px;top:71px">AGB</div>
  <div class="abs f-link" style="left:247px;top:89px">Impressum</div>

  <div class="abs f-h" style="left:344px;top:37px">Rückrufservice</div>
  <div class="abs f-text" style="left:344px;top:51px">Wir rufen Sie schnellst möglich<br>an und helfen Ihnen weiter!</div>
  <div class="abs f-input" style="left:343px;top:79px">Ihr Name</div>
  <div class="abs f-input" style="left:343px;top:97px">Telefonnummer</div>
  <div class="abs f-btn" style="left:343px;top:118px">absenden</div>

  <div class="abs" style="left:481px;top:38px;display:flex;align-items:center;gap:4px;font-size:10px;font-weight:700"><span style="width:7px;height:7px;background:#fff"></span>KESTNER DACHBAU</div>
  <svg class="abs" style="left:481px;top:76px" width="7" height="8" viewBox="0 0 7 8" fill="none" stroke="#fff" stroke-width=".8"><path d="M3.5 7.5S1 4.8 1 3a2.5 2.5 0 0 1 5 0c0 1.8-2.5 4.5-2.5 4.5z"/><circle cx="3.5" cy="3" r=".9"/></svg>
  <div class="abs f-link" style="left:493px;top:75px">Lindenweg 7, 55411 Hohenau</div>
  <svg class="abs" style="left:481px;top:89px" width="7" height="6" viewBox="0 0 7 6" fill="none" stroke="#fff" stroke-width=".8"><rect x=".5" y=".5" width="6" height="5"/><path d="M.5 .5l3 2.5 3-2.5"/></svg>
  <div class="abs f-link" style="left:493px;top:87px">info@kestner-dachbau.example</div>
  <svg class="abs" style="left:481px;top:100px" width="7" height="7" viewBox="0 0 7 7" fill="none" stroke="#fff" stroke-width=".8"><path d="M1.5.5l1.3 1.3-.8.9c.5 1 1.2 1.7 2.2 2.2l.9-.8 1.3 1.3-.9 1C2.8 6 1 4.2.5 1.4z"/></svg>
  <div class="abs f-link" style="left:493px;top:99px">06214 - 57 20 48</div>
  <div class="abs social" style="left:480px;top:120px"></div>
  <div class="abs social" style="left:496px;top:120px"></div>
  <div class="abs social" style="left:512px;top:120px"></div>
</footer>

</body>
</html>
```